Art Deco Wedding Invitation

We need a wedding invitation designed for a 1920's Art Deco theme.
The wedding will take place in Berlin, which had a glamorous, modern and wild culture in the 1920's. This may offer some design inspiration.
The couple's names are Rowan and Liesel and the wedding will take place on May 8, 2015.

Industry/Entity Type

Wedding

```html
<!DOCTYPE html>
<html lang="en">
<head>
<meta charset="utf-8">
<title>Rowan &amp; Liesel – Wedding Invitation</title>
<link rel="stylesheet" href="https://fonts.googleapis.com/css2?family=Cormorant+Garamond:wght@500&family=Poiret+One&display=swap">
<style>
  :root {
    --backdrop: #d1d2d4;
    --paper: #ffffff;
    --gold: #c49a62;
    --gold-light: #e3cba8;
    --gold-pale: #f4ead9;
  }
  html, body {
    margin: 0;
    padding: 0;
    overflow: hidden;
  }
  .canvas {
    position: relative;
    width: 1200px;
    height: 881px;
    background: var(--backdrop);
    overflow: hidden;
  }
  .card {
    position: absolute;
    top: 98px;
    width: 490px;
    height: 684px;
    background: var(--paper);
  }
  .card--cover { left: 98px; }
  .card--details { left: 612px; }

  .cover-pattern {
    position: absolute;
    left: 24px;
    top: 22px;
    width: 442px;
    height: 640px;
    background:
      linear-gradient(135deg, var(--gold-pale) 0%, var(--gold-light) 50%, var(--gold-pale) 100%);
    outline: 3px solid var(--gold);
  }
  .monogram-plate {
    position: absolute;
    left: 132px;
    top: 194px;
    width: 226px;
    height: 124px;
    background: var(--paper);
  }
  .monogram {
    position: absolute;
    left: 0;
    right: 0;
    top: 0;
    bottom: 0;
    display: flex;
    align-items: center;
    justify-content: center;
    font-family: "Poiret One", sans-serif;
    font-size: 50px;
    color: var(--gold);
    letter-spacing: 2px;
  }

  .frame-lines {
    position: absolute;
    left: 0;
    top: 0;
  }

  .invite-text {
    position: absolute;
    left: 0;
    width: 490px;
    margin: 0;
    text-align: center;
    font-family: "Cormorant Garamond", serif;
    font-weight: 500;
    font-size: 11.5px;
    line-height: 19px;
    letter-spacing: 1.6px;
    text-transform: uppercase;
    color: var(--gold);
  }
  .invite-text--hosts { top: 92px; }
  .invite-text--request { top: 276px; }
  .invite-text--when { top: 336px; }
  .invite-text--where { top: 435px; }
  .invite-text--after { top: 570px; }

  .couple-names {
    position: absolute;
    left: 0;
    width: 490px;
    top: 162px;
    margin: 0;
    text-align: center;
    font-family: "Poiret One", sans-serif;
    font-weight: 400;
    font-size: 42px;
    line-height: 52px;
    letter-spacing: 3px;
    text-transform: uppercase;
    color: var(--gold);
  }
</style>
</head>
<body>
<main class="canvas">

  <section class="card card--cover">
    <div class="cover-pattern" role="img" aria-label="Gold Art Deco geometric line pattern of stepped blocks and diagonal rays"></div>
    <div class="monogram-plate">
      <svg class="frame-lines" width="226" height="124" viewBox="0 0 226 124" aria-hidden="true">
        <rect x="1.5" y="1.5" width="223" height="121" fill="none" stroke="var(--gold)" stroke-width="3"/>
        <rect x="9" y="9" width="208" height="106" fill="none" stroke="var(--gold)" stroke-width="1.2"/>
        <rect x="20" y="20" width="186" height="84" fill="none" stroke="var(--gold)" stroke-width="1"/>
      </svg>
      <div class="monogram">R+L</div>
    </div>
  </section>

  <section class="card card--details">
    <svg class="frame-lines" width="490" height="684" viewBox="0 0 490 684" aria-hidden="true">
      <g fill="none" stroke="var(--gold)">
        <rect x="24" y="24" width="442" height="636" stroke-width="3"/>
        <rect x="32" y="32" width="426" height="620" stroke-width="1.5"/>
        <rect x="44" y="42" width="402" height="600" stroke-width="1"/>
        <rect x="22" y="22" width="18" height="18" stroke-width="1.5"/>
        <rect x="450" y="22" width="18" height="18" stroke-width="1.5"/>
        <rect x="22" y="644" width="18" height="18" stroke-width="1.5"/>
        <rect x="450" y="644" width="18" height="18" stroke-width="1.5"/>
        <line x1="86" y1="134" x2="392" y2="134" stroke-width="1"/>
        <line x1="86" y1="140" x2="404" y2="140" stroke-width="1"/>
        <line x1="96" y1="146" x2="404" y2="146" stroke-width="1"/>
        <line x1="86" y1="230" x2="394" y2="230" stroke-width="1"/>
        <line x1="86" y1="236" x2="404" y2="236" stroke-width="1"/>
        <line x1="96" y1="242" x2="404" y2="242" stroke-width="1"/>
      </g>
    </svg>

    <p class="invite-text invite-text--hosts">Together with their families</p>
    <h1 class="couple-names">Rowan &amp; Liesel</h1>
    <p class="invite-text invite-text--request">Invite you to celebrate their marriage</p>
    <p class="invite-text invite-text--when">Friday the eighth of May<br>Two thousand fifthteen<br>At one o’clock in the afternoon</p>
    <p class="invite-text invite-text--where">The Grand Hotel<br>12345 Main Street<br>City, State/Country</p>
    <p class="invite-text invite-text--after">- Dinner &amp; dancing to follow -</p>
  </section>

</main>
</body>
</html>
```